Shine Bay Auto Care Business Card

2 side business card design for an auto detailing business

Target Market(s)

Auto detailing

Contact Information for Business Card

Things included

The business name “Shine Bay Auto Care”
Marc Tessier
(555)261-9047
Riverton, Sk

Services offered - complete interior& exterior detail
- paint correction & protection
- ceramic coating
- trim restore
- auto carpet & seat cleaning

Requirements
Must have
• Colours that are in my logo

Services offered

My name Marc Tessier
403-261-9047
Riverton, Sk

Not too sure in what order for these ?
Website. Shinebayautocare.com
Instagram Shinebayautocare
Email. Shinebayautoac@mailbox-example.com

```html
<!DOCTYPE html>
<html lang="en">
<head>
<meta charset="utf-8">
<title>Shine Bay Auto Care – Business Card</title>
<link href="https://fonts.googleapis.com/css2?family=Montserrat:wght@400;500;600;700&display=swap" rel="stylesheet">
<style>
  :root {
    --brand-red: #9e0f12;
    --ink: #1b1b1b;
    --card-black: #1d1d1e;
    --paper: #ffffff;
    --backdrop: #d9d9d9;
    --muted: #4a4a4a;
  }
  * { box-sizing: border-box; margin: 0; padding: 0; }
  html, body { width: 899px; height: 1200px; overflow: hidden; }
  body {
    background: var(--backdrop);
    font-family: "Montserrat", Arial, sans-serif;
    position: relative;
  }
  .card-set { position: absolute; left: 0; width: 899px; height: 600px; }
  .card-set--main { top: 0; }
  .card-set--alt { top: 600px; }

  .card {
    position: absolute;
    width: 420px;
    height: 240px;
    border-radius: 14px;
    border-bottom: 3px solid var(--brand-red);
    overflow: hidden;
    box-shadow: 0 10px 24px rgba(0,0,0,0.18);
  }
  .card--front { left: 24px; top: 80px; background: var(--paper); }
  .card--back { left: 455px; top: 300px; background: var(--card-black); }

  /* Front */
  .brand {
    position: absolute;
    right: 40px;
    top: 40px;
    display: flex;
    align-items: center;
    gap: 10px;
  }
  .brand__dot {
    width: 34px; height: 34px;
    border-radius: 50%;
    border: 4px solid var(--brand-red);
  }
  .brand__name {
    font-weight: 600;
    font-size: 17px;
    letter-spacing: 1.5px;
    text-transform: uppercase;
    color: var(--ink);
    line-height: 1.15;
  }
  .website {
    position: absolute;
    right: 30px;
    bottom: 30px;
    font-size: 10px;
    color: var(--brand-red);
  }
  .person {
    position: absolute;
    left: 30px;
    bottom: 28px;
  }
  .person__name {
    font-weight: 600;
    font-size: 15px;
    letter-spacing: 0.5px;
    text-transform: uppercase;
    color: var(--brand-red);
    margin-bottom: 6px;
  }
  .contact-list { list-style: none; }
  .contact-list li {
    display: flex;
    align-items: center;
    gap: 6px;
    font-size: 9.5px;
    color: var(--muted);
    line-height: 14px;
  }
  .contact-list svg { width: 9px; height: 9px; flex: none; }

  /* Back */
  .back-brand {
    position: absolute;
    left: 0; right: 0;
    top: 48px;
    display: flex;
    justify-content: center;
    align-items: center;
    gap: 10px;
  }
  .back-brand__dot {
    width: 40px; height: 40px;
    border-radius: 50%;
    border: 5px solid var(--brand-red);
  }
  .back-brand__name {
    font-weight: 600;
    font-size: 20px;
    letter-spacing: 1.5px;
    text-transform: uppercase;
    color: var(--brand-red);
  }
  .services {
    position: absolute;
    left: 0; right: 0;
    bottom: 40px;
    text-align: center;
  }
  .services__title {
    font-weight: 700;
    font-size: 11.5px;
    color: var(--paper);
    letter-spacing: 0.3px;
    margin-bottom: 5px;
  }
  .services__line {
    font-size: 10.5px;
    color: var(--brand-red);
    line-height: 14px;
  }
</style>
</head>
<body>

<section class="card-set card-set--main">
  <article class="card card--front">
    <div class="brand">
      <span class="brand__dot"></span>
      <span class="brand__name">Shine Bay<br>Auto Care</span>
    </div>
    <div class="person">
      <p class="person__name">Marc Tessier</p>
      <ul class="contact-list">
        <li><svg viewBox="0 0 10 10"><path d="M5 0a3.5 3.5 0 0 0-3.5 3.5C1.5 6 5 10 5 10s3.5-4 3.5-6.5A3.5 3.5 0 0 0 5 0zm0 5a1.4 1.4 0 1 1 0-2.8A1.4 1.4 0 0 1 5 5z" fill="#9e0f12"/></svg>Riverton, Sk</li>
        <li><svg viewBox="0 0 10 10"><path d="M2 0.5l2 2-1 1.2c.6 1.3 1.6 2.3 2.9 2.9L7 5.6l2 2-1.2 1.9C4.5 9.3.7 5.5.5 2.2z" fill="#9e0f12"/></svg>(555)261-9047</li>
        <li><svg viewBox="0 0 10 10"><rect x="0.5" y="2" width="9" height="6.5" fill="#9e0f12"/><path d="M0.5 2l4.5 3.5L9.5 2" stroke="#fff" stroke-width="0.8" fill="none"/></svg>shinebayautoac@mailbox-example.com</li>
        <li><svg viewBox="0 0 10 10"><circle cx="5" cy="5" r="4" fill="none" stroke="#9e0f12" stroke-width="1.4"/></svg>shinebayautocare</li>
      </ul>
    </div>
    <p class="website">www.shinebayautocare.com</p>
  </article>

  <article class="card card--back">
    <div class="back-brand">
      <span class="back-brand__dot"></span>
      <span class="back-brand__name">Shine Bay Auto Care</span>
    </div>
    <div class="services">
      <p class="services__title">COMPLETE MOBILE AUTO DETAILING</p>
      <p class="services__line">Paint correction &amp; Protection • Ceramic Coating</p>
      <p class="services__line">Auto Carpet &amp; Seat Cleaning • Trim Restore</p>
    </div>
  </article>
</section>

<section class="card-set card-set--alt">
  <article class="card card--front">
    <div class="brand">
      <span class="brand__dot"></span>
      <span class="brand__name">Shine Bay<br>Auto Care</span>
    </div>
    <div class="person">
      <p class="person__name">Marc Tessier</p>
      <ul class="contact-list">
        <li><svg viewBox="0 0 10 10"><path d="M5 0a3.5 3.5 0 0 0-3.5 3.5C1.5 6 5 10 5 10s3.5-4 3.5-6.5A3.5 3.5 0 0 0 5 0zm0 5a1.4 1.4 0 1 1 0-2.8A1.4 1.4 0 0 1 5 5z" fill="#9e0f12"/></svg>Pinecrest, Ab</li>
        <li><svg viewBox="0 0 10 10"><path d="M2 0.5l2 2-1 1.2c.6 1.3 1.6 2.3 2.9 2.9L7 5.6l2 2-1.2 1.9C4.5 9.3.7 5.5.5 2.2z" fill="#9e0f12"/></svg>(555)261-9047</li>
        <li><svg viewBox="0 0 10 10"><rect x="0.5" y="2" width="9" height="6.5" fill="#9e0f12"/><path d="M0.5 2l4.5 3.5L9.5 2" stroke="#fff" stroke-width="0.8" fill="none"/></svg>shinebayautoac@mailbox-example.com</li>
        <li><svg viewBox="0 0 10 10"><circle cx="5" cy="5" r="4" fill="none" stroke="#9e0f12" stroke-width="1.4"/></svg>shinebayautocare</li>
      </ul>
    </div>
    <p class="website">www.shinebayautocare.com</p>
  </article>

  <article class="card card--back">
    <div class="back-brand">
      <span class="back-brand__dot"></span>
      <span class="back-brand__name">Shine Bay Auto Care</span>
    </div>
    <div class="services">
      <p class="services__title">COMPLETE MOBILE AUTO DETAILING</p>
      <p class="services__line">Paint correction &amp; Protection • Ceramic Coating</p>
      <p class="services__line">Auto Carpet &amp; Seat Cleaning • Trim Restore</p>
    </div>
  </article>
</section>

</body>
</html>
```